HVRT LLP website - revamping our website after 23 years

Our website needs a complete overhaul. The purpose of this exercise is to provide us with your vision of what you think the website should look like. We don't need the website to be created or coded. Just need creative designs.

We have a four sites that we would like to base our website on;

We like the simplicity of Ravelstoke, the style of Pemberly Adair and Quillfeather.

http://www.pemberlyadair.example/en/toronto-ontario/
http://www.ravelstoke.example/
vintquillfeather.example
http://www.brindlemoor.example/our-professionals.html

We have a logo that we would like to use which will be attached below. We need to keep our website looking very professional as we have a large number of high net worth clients.
Updates

Hi, We've received some good website designs but they appear to be the same type of template websites we've received in the past - this is not what we're looking for. What we want is a unique website that is modelled on the following three company websites: http://www.ravelstoke.example/ www.vintquillfeather.example/ http://www.pemberlyadair.example/en/toronto-ontario/

Thank you everyone for your designs. I will be posting updates and my comments on the various designs in the next day - I want to thank you for the creative designs I see. I thought i would explain a bit about our firm and perhaps it can help when you design the theme of our website: - Our firm is like a family and our clients are truly like our friends. We have close knit relationships in and outside of the office with staff and clients. - We are an 'out of the box' type of firm. We operate differently than most firms and that's a differentiating factor in what makes us who we are - Our slogan is "Count on us" which is a testament to the way we run our practice - We would like an open, fresh, clean look to our website - we don't want the landing page to be overly long or complex because we have limited time to update the website and limited content That's it for the time being - when things come to mind I will post them here.

Can we try a design as follows: - make the website look very similar to www.ravelstoke.example - use the same background colour - Keep the same black top but insert our logo - incorporate some of the content from our current website www.hvrt-ca.example

I have been away dealing with a personal matter. I will look into these websites tomorrow afternoon and provide more feedback / info on the top designer. Thank you

Hi designers, I want to apologize for the delay. I plan on wrapping things up within the next few days. I will go through a few of the top designs and offer my comments. Thank you for your patience.

Target Market(s)

Mainly our current clients - We have a large number of high net worth individuals as clients.

Industry/Entity Type

Accounting

Number of Pages Required

1 page

Requirements
Must have
• Please model website on the websites indicated above.
• Our current website is www.hvrt-ca.example. It's dark, cluttered and not inviting. We want a fresh, clean website. Please incorporate the logo's attached below.

```html
<!DOCTYPE html>
<html lang="en">
<head>
<meta charset="utf-8">
<title>HVRT LLP — Chartered Professional Accountants</title>
<link rel="stylesheet" href="https://fonts.googleapis.com/css2?family=Cinzel:wght@400;700&family=Raleway:wght@400;600;700&display=swap">
<style>
  :root {
    --ink-black: #111113;
    --header-dark: #1e1f22;
    --footer-dark: #161618;
    --bottom-bar: #232326;
    --sky-deep: #1c6f9c;
    --sky-mid: #2a9fd8;
    --sky-light: #56bde8;
    --band-teal: #1b6a8c;
    --accent-blue: #1ea3e0;
    --leaf-green: #8dc63f;
    --berry: #a1206b;
    --violet: #6b2a8f;
    --white: #ffffff;
    --soft-white: #e6eef3;
  }
  * { box-sizing: border-box; margin: 0; padding: 0; }
  html, body { width: 1200px; height: 1035px; overflow: hidden; background: var(--ink-black); }
  body { position: relative; font-family: "Raleway", sans-serif; color: var(--white); }

  .utility-bar { position: absolute; top: 0; left: 0; width: 1200px; height: 26px; background: var(--ink-black);
    font-size: 13px; display: flex; justify-content: flex-end; align-items: center; gap: 36px; padding-right: 164px; }
  .utility-bar span { display: flex; align-items: center; gap: 7px; }

  .site-header { position: absolute; top: 26px; left: 0; width: 1200px; height: 91px;
    background: linear-gradient(180deg, #2a2b2e, var(--header-dark)); }
  .brand { position: absolute; left: 146px; top: 24px; display: flex; align-items: center; gap: 10px;
    font-family: "Cinzel", serif; font-size: 33px; color: var(--white); letter-spacing: 0.5px; }
  .brand-mark { width: 44px; height: 44px; border: 3px solid var(--accent-blue); }
  .main-nav { position: absolute; left: 417px; top: 32px; display: flex; align-items: center;
    font-family: "Cinzel", serif; font-size: 15px; letter-spacing: 0.8px; }
  .main-nav a { color: var(--white); text-decoration: none; padding: 3px 10px 4px; border-right: 1px solid #55575c; line-height: 17px; }
  .main-nav a:last-child { border-right: 0; }
  .main-nav a.current { background: var(--accent-blue); border-right: 0; margin-right: 6px; padding: 4px 9px 3px; }

  .hero { position: absolute; top: 117px; left: 0; width: 1200px; height: 541px; overflow: hidden;
    background: linear-gradient(170deg, var(--sky-deep) 0%, #1f86bd 45%, var(--sky-mid) 75%, var(--sky-light) 100%); }
  .hero-photo { position: absolute; right: 0; top: 0; width: 560px; height: 541px;
    background: radial-gradient(ellipse at 65% 55%, rgba(40,50,70,0.85) 0%, rgba(60,90,120,0.55) 40%, rgba(42,140,200,0) 75%); }
  .hero-headline { position: absolute; left: 162px; top: 66px; font-family: "Cinzel", serif; font-weight: 700; line-height: 46px; }
  .hero-headline .line-lg { font-size: 36px; display: block; }
  .hero-headline .line-lg small { font-size: 25px; }
  .hero-headline .line-sm { font-size: 25px; display: block; line-height: 37px; letter-spacing: 1px; }
  .read-more { position: absolute; left: 162px; top: 261px; width: 110px; height: 31px; background: #2b2b2c;
    border: 1px solid #0f0f10; border-radius: 2px; font-family: "Cinzel", serif; font-size: 14px;
    display: flex; align-items: center; justify-content: center; letter-spacing: 0.5px; }

  .feature-band { position: absolute; top: 658px; left: 0; width: 1200px; height: 202px;
    background: linear-gradient(90deg, #1c5f7e, var(--band-teal) 50%, #17678c); }
  .feature { position: absolute; top: 72px; width: 280px; text-align: center; }
  .feature h2 { font-family: "Cinzel", serif; font-weight: 400; font-size: 29px; letter-spacing: 1px; line-height: 34px; }
  .feature p { font-size: 14px; line-height: 19.5px; color: var(--soft-white); margin-top: 2px; }
  .feature .expand { display: block; margin: 9px auto 0; }
  .feature-about { left: 168px; }
  .feature-services { left: 460px; }
  .feature-careers { left: 752px; }

  .diamond { position: absolute; top: 592px; width: 134px; height: 134px; }

  .site-footer { position: absolute; top: 860px; left: 0; width: 1200px; height: 130px; background: var(--footer-dark); }
  .address { position: absolute; left: 162px; top: 40px; display: flex; gap: 10px; font-size: 13px; line-height: 17.5px; }
  .address strong { font-weight: 700; font-size: 14px; }
  .contact-line { position: absolute; left: 468px; display: flex; align-items: center; gap: 18px; font-size: 14px; }
  .footer-brand { position: absolute; left: 800px; top: 45px; display: flex; align-items: center; gap: 10px;
    font-family: "Cinzel", serif; font-size: 31px; }
  .footer-brand .brand-mark { width: 40px; height: 40px; border-color: var(--white); }

  .bottom-bar { position: absolute; top: 990px; left: 0; width: 1200px; height: 45px; background: var(--bottom-bar); }
  .copyright { position: absolute; left: 163px; top: 16px; font-size: 11.5px; color: #d8d8d8; }
  .social { position: absolute; left: 805px; top: 6px; display: flex; gap: 14px; }
  .social span { width: 33px; height: 33px; border-radius: 50%; border: 2px solid #d0d3d8; }
</style>
</head>
<body>
  <div class="utility-bar">
    <span>
      <svg width="14" height="14" viewBox="0 0 24 24"><path fill="#fff" d="M6.6 10.8a15.1 15.1 0 0 0 6.6 6.6l2.2-2.2c.3-.3.7-.4 1-.2 1.1.4 2.3.6 3.6.6.6 0 1 .4 1 1V20c0 .6-.4 1-1 1A17 17 0 0 1 3 4c0-.6.4-1 1-1h3.5c.6 0 1 .4 1 1 0 1.3.2 2.5.6 3.6.1.3 0 .7-.2 1z"/></svg>
      (416) 555-0142
    </span>
    <span>
      <svg width="18" height="12" viewBox="0 0 18 12"><rect width="18" height="12" fill="#fff"/><path d="M0 0l9 7 9-7" stroke="#111" stroke-width="1.4" fill="none"/></svg>
      info@hvrt-ca.example
    </span>
  </div>

  <header class="site-header">
    <div class="brand"><span class="brand-mark"></span>HVRT LLP</div>
    <nav class="main-nav">
      <a class="current">Home</a>
      <a>About HVRT</a>
      <a>Services</a>
      <a>Library</a>
      <a>Links</a>
      <a>Careers</a>
      <a>Contact Us</a>
    </nav>
  </header>

  <section class="hero">
    <div class="hero-photo" role="img" aria-label="Photo of a smiling accountant in a suit reading a tablet, colleagues blurred behind him"></div>
    <h1 class="hero-headline">
      <span class="line-lg">Together, <small>WE BRING OVER</small> 100</span>
      <span class="line-lg">Years <small>OF VALUABLE EXPERIENCE</small></span>
      <span class="line-sm">TO THE PRACTICE OF PUBLIC</span>
      <span class="line-sm">ACCOUNTING</span>
    </h1>
    <div class="read-more">Read More</div>
  </section>

  <section class="feature-band">
    <div class="feature feature-about">
      <h2>About HVRT</h2>
      <p>HVRT, like any good organization is comprised of its people. Its partners. And its staff.</p>
      <svg class="expand" width="20" height="20" viewBox="0 0 20 20"><rect width="20" height="20" fill="#fff"/><path d="M10 4v12M4 10h12" stroke="#1b6a8c" stroke-width="3"/></svg>
    </div>
    <div class="feature feature-services">
      <h2>Our Services</h2>
      <p>We Offer Full Services Public Accounting With the Personal Touch of a Small Firm</p>
      <svg class="expand" width="20" height="20" viewBox="0 0 20 20"><rect width="20" height="20" fill="#fff"/><path d="M10 4v12M4 10h12" stroke="#1b6a8c" stroke-width="3"/></svg>
    </div>
    <div class="feature feature-careers">
      <h2>Careers</h2>
      <p>HVRT, like any good organization is comprised of its people. Its partners. And its staff.</p>
      <svg class="expand" width="20" height="20" viewBox="0 0 20 20"><rect width="20" height="20" fill="#fff"/><path d="M10 4v12M4 10h12" stroke="#1b6a8c" stroke-width="3"/></svg>
    </div>
  </section>

  <svg class="diamond" style="left:241px" viewBox="0 0 134 134">
    <rect x="22" y="22" width="90" height="90" transform="rotate(45 67 67)" fill="var(--leaf-green)" stroke="#fff" stroke-width="4"/>
    <rect x="51" y="51" width="32" height="32" fill="none" stroke="#fff" stroke-width="4"/>
  </svg>
  <svg class="diamond" style="left:533px" viewBox="0 0 134 134">
    <rect x="22" y="22" width="90" height="90" transform="rotate(45 67 67)" fill="var(--berry)" stroke="#fff" stroke-width="4"/>
    <rect x="56" y="48" width="26" height="36" rx="2" fill="none" stroke="#fff" stroke-width="3"/>
    <rect x="60" y="52" width="18" height="7" fill="#fff"/>
    <g fill="#fff"><rect x="60" y="63" width="4" height="4"/><rect x="67" y="63" width="4" height="4"/><rect x="74" y="63" width="4" height="4"/><rect x="60" y="70" width="4" height="4"/><rect x="67" y="70" width="4" height="4"/><rect x="74" y="70" width="4" height="4"/><rect x="60" y="77" width="4" height="4"/><rect x="67" y="77" width="4" height="4"/><rect x="74" y="77" width="4" height="4"/></g>
    <text x="52" y="63" font-family="Raleway, sans-serif" font-weight="700" font-size="20" fill="#fff" text-anchor="middle">$</text>
  </svg>
  <svg class="diamond" style="left:825px" viewBox="0 0 134 134">
    <rect x="22" y="22" width="90" height="90" transform="rotate(45 67 67)" fill="var(--violet)" stroke="#fff" stroke-width="4"/>
    <rect x="62" y="50" width="12" height="7" rx="2" fill="none" stroke="#fff" stroke-width="3"/>
    <rect x="50" y="56" width="36" height="24" rx="3" fill="#fff"/>
    <path d="M50 66h36" stroke="var(--violet)" stroke-width="2"/>
  </svg>

  <footer class="site-footer">
    <div class="address">
      <svg width="19" height="26" viewBox="0 0 19 26"><path fill="#fff" d="M9.5 0A9.5 9.5 0 0 0 0 9.5C0 16 9.5 26 9.5 26S19 16 19 9.5A9.5 9.5 0 0 0 9.5 0zm0 13a3.5 3.5 0 1 1 0-7 3.5 3.5 0 0 1 0 7z"/></svg>
      <div>
        <strong>HVRT LLP</strong><br>
        Harbourview Centre 2180 Linden Street<br>
        Suite 1402 Toronto, Ontario<br>
        Canada, M4B 2T7
      </div>
    </div>
    <div class="contact-line" style="top:40px">
      <svg width="24" height="16" viewBox="0 0 24 16"><rect width="24" height="16" fill="#fff"/><path d="M0 0l12 9 12-9M0 16l9-8M24 16l-9-8" stroke="#161618" stroke-width="1.5" fill="none"/></svg>
      info@hvrt-ca.example
    </div>
    <div class="contact-line" style="top:82px">
      <svg width="22" height="22" viewBox="0 0 24 24"><path fill="#fff" d="M6.6 10.8a15.1 15.1 0 0 0 6.6 6.6l2.2-2.2c.3-.3.7-.4 1-.2 1.1.4 2.3.6 3.6.6.6 0 1 .4 1 1V20c0 .6-.4 1-1 1A17 17 0 0 1 3 4c0-.6.4-1 1-1h3.5c.6 0 1 .4 1 1 0 1.3.2 2.5.6 3.6.1.3 0 .7-.2 1z"/></svg>
      (416) 555-0142
    </div>
    <div class="footer-brand"><span class="brand-mark"></span>HVRT LLP</div>
  </footer>

  <div class="bottom-bar">
    <p class="copyright">Copyright 2015 HVRT LLP . All rights reserved.</p>
    <div class="social" aria-label="Social links">
      <span style="background:#3b5998"></span>
      <span style="background:#2aa3e0"></span>
      <span style="background:#1f7bb6"></span>
      <span style="background:#d63b2f"></span>
    </div>
  </div>
</body>
</html>
```